Pricing Page; Request Quote Page Design

I'm looking to update our pricing page and request page to something more modern in terms of the layout/form design and with more content, but needs to be consistent with the rest of our site. I need two pages designed. 1) A general pricing page w/ CTAs for quotes, and 2) The request quote page with form. Ideally there would be (3) parts for our different packages (Express, Professional, Enterprise) on the pricing page, with CTAs on each section. I like the hero image approach used here https://quillmarsh.com/pricing and here http://www.darkfennel.com/wp-content/uploads/2016/08/grovetalk-pricing-page-design.png In terms of the form page, mainly just looking for an improvement over this https://www.pebbleworkshop.com/price-quote-request

I also included a sample mockup to provide a BIT of guidance, but looking for something a little different and modern.

Industry/Entity Type

Pricing

Number of Pages Required

2 page

Font styles to use
Sans Serif

Requirements
Must have
• Hero background image on main pricing page. Needs to follow the look and feel of pebbleworkshop.com

```html
<!DOCTYPE html>
<html lang="en">
<head>
<meta charset="utf-8">
<title>Pricing — Pebble Workshop</title>
<link href="https://fonts.googleapis.com/css2?family=Raleway:wght@300;400;500;600;700;800&display=swap" rel="stylesheet">
<style>
  :root {
    --bar: #2b2b2b;
    --ink: #232323;
    --green: #6cc100;
    --green-soft: #86c540;
    --green-deep: #76a03a;
    --page: #f4f5f5;
    --white: #ffffff;
    --nav-text: #d8d8d8;
  }
  * { box-sizing: border-box; margin: 0; padding: 0; }
  html, body { width: 1200px; height: 975px; overflow: hidden; }
  body {
    position: relative;
    background: var(--page);
    font-family: "Raleway", sans-serif;
    color: var(--ink);
  }
  .site-header {
    position: absolute; left: 0; top: 0; width: 1200px; height: 113px;
    background: var(--bar);
  }
  .call-line {
    position: absolute; left: 855px; top: 18px;
    color: var(--green); font-weight: 700; font-size: 15px;
  }
  .demo-button {
    position: absolute; left: 1041px; top: 13px; width: 131px; height: 33px;
    background: var(--green); color: var(--white);
    font-weight: 700; font-size: 13px; letter-spacing: -0.2px;
    display: flex; align-items: center; justify-content: center;
  }
  .brand {
    position: absolute; left: 27px; top: 64px; height: 27px;
    display: flex; align-items: center;
    font-weight: 600; font-size: 20px; color: var(--white);
  }
  .main-nav {
    position: absolute; left: 440px; top: 75px; width: 736px;
    display: flex; justify-content: space-between;
    font-size: 13.5px; letter-spacing: 2.6px; color: var(--nav-text); font-weight: 500;
  }
  .hero {
    position: absolute; left: 0; top: 113px; width: 1200px; height: 531px;
    background:
      radial-gradient(circle at 72% 48%, rgba(0,200,130,0.45), transparent 32%),
      radial-gradient(circle at 85% 20%, rgba(60,110,90,0.6), transparent 30%),
      linear-gradient(160deg, #27352a 0%, #2f4a35 45%, #1c2e26 100%);
  }
  .hero-copy {
    position: absolute; left: 0; top: 312px; width: 1200px; text-align: center; color: var(--white);
  }
  .hero-copy h1 {
    font-weight: 300; font-size: 41px; letter-spacing: 0.4px; line-height: 1;
  }
  .hero-copy p {
    margin-top: 32px; font-size: 16.5px; line-height: 26px; font-weight: 500;
  }
  .plan {
    position: absolute; top: 555px; width: 299px; height: 360px;
    background: var(--white); border: 1px solid #dcdcdc;
  }
  .plan.express { left: 137px; }
  .plan.professional { left: 451px; }
  .plan.enterprise { left: 765px; }
  .plan-name {
    height: 39px; display: flex; align-items: center; justify-content: center;
    font-size: 19px; color: var(--white); font-weight: 500;
  }
  .express .plan-name { background: var(--green); }
  .professional .plan-name { background: var(--ink); }
  .enterprise .plan-name { background: var(--green-soft); }
  .plan-scope {
    margin-top: 16px; text-align: center; font-size: 18.5px; font-weight: 400;
  }
  .price {
    margin-top: 22px; text-align: center; font-weight: 300; line-height: 1;
    display: flex; align-items: baseline; justify-content: center;
  }
  .price .cur { font-size: 29px; }
  .price .whole { font-size: 62px; letter-spacing: -1px; }
  .price .cents { font-size: 28px; }
  .express .plan-scope, .express .price, .express .features { color: var(--green); }
  .enterprise .plan-scope, .enterprise .price, .enterprise .features { color: var(--green-soft); }
  .features { position: absolute; left: 18px; top: 189px; right: 6px; }
  .professional .features, .enterprise .features { top: 192px; }
  .features h3 { font-size: 13.5px; font-weight: 500; margin-bottom: 9px; }
  .features ul { list-style: none; }
  .features li {
    display: flex; gap: 10px; font-size: 13px; font-weight: 800; line-height: 18px; margin-bottom: 4px;
  }
  .express .features li { margin-bottom: 4.5px; }
  .professional .features li, .enterprise .features li { margin-bottom: 0; }
  .features svg { flex: none; margin-top: 3px; }
  .quote-button {
    position: absolute; left: -1px; right: -1px; bottom: -1px; height: 40px;
    display: flex; align-items: center; justify-content: center;
    color: var(--white); font-size: 19px; font-weight: 500;
  }
  .express .quote-button { background: var(--green); }
  .professional .quote-button { background: var(--ink); }
  .enterprise .quote-button { background: var(--green-deep); }
</style>
</head>
<body>
  <header class="site-header">
    <div class="call-line">CALL 1-866-555-0142</div>
    <div class="demo-button">REQUEST DEMO</div>
    <div class="brand">Pebble Workshop</div>
    <nav class="main-nav">
      <span>FEATURES</span><span>SERVICES</span><span>PRICING</span><span>RESOURCES</span><span>BLOG</span><span>NEWS</span><span>CONTACT</span>
    </nav>
  </header>

  <section class="hero" role="img" aria-label="Dark green 3D city of blocks with glowing neon circuit lines and a striped sphere on a pedestal"></section>
  <div class="hero-copy">
    <h1>Flexible Pricing Designed to Fit Your Business</h1>
    <p>Our pay-as-you-grow pricing model is geared to minimize risk and maximize return.<br>
    Whether launching a new learning initiative, or looking to migrate (or integrate) an<br>
    existing business with our Learning Business Platform, we have you covered.</p>
  </div>

  <article class="plan express">
    <div class="plan-name">EXPRESS</div>
    <div class="plan-scope">Less than 25 courses</div>
    <div class="price"><span class="cur">$</span><span class="whole">499</span><span class="cents">.00</span></div>
    <div class="features">
      <h3>Express Features:</h3>
      <ul>
        <li><svg width="16" height="12" viewBox="0 0 16 12"><path d="M1 6h13M9 1l5 5-5 5" fill="none" stroke="currentColor" stroke-width="2"/></svg>Launch in weeks, not months</li>
        <li><svg width="16" height="12" viewBox="0 0 16 12"><path d="M1 6h13M9 1l5 5-5 5" fill="none" stroke="currentColor" stroke-width="2"/></svg>Perfect for smaller businesses</li>
        <li><svg width="16" height="12" viewBox="0 0 16 12"><path d="M1 6h13M9 1l5 5-5 5" fill="none" stroke="currentColor" stroke-width="2"/></svg>Less than 1,000 users</li>
        <li><svg width="16" height="12" viewBox="0 0 16 12"><path d="M1 6h13M9 1l5 5-5 5" fill="none" stroke="currentColor" stroke-width="2"/></svg>Less than 25 courses.</li>
      </ul>
    </div>
    <div class="quote-button">REQUEST QUOTE</div>
  </article>

  <article class="plan professional">
    <div class="plan-name">PROFESSINOAL</div>
    <div class="plan-scope">Upto 100 courses</div>
    <div class="price"><span class="cur">$</span><span class="whole">789</span><span class="cents">.00</span></div>
    <div class="features">
      <h3>Professional Features:</h3>
      <ul>
        <li><svg width="16" height="12" viewBox="0 0 16 12"><path d="M1 6h13M9 1l5 5-5 5" fill="none" stroke="currentColor" stroke-width="2"/></svg>Designed for more established learning businesses</li>
        <li><svg width="16" height="12" viewBox="0 0 16 12"><path d="M1 6h13M9 1l5 5-5 5" fill="none" stroke="currentColor" stroke-width="2"/></svg>Scale &amp; leverage modern technology</li>
        <li><svg width="16" height="12" viewBox="0 0 16 12"><path d="M1 6h13M9 1l5 5-5 5" fill="none" stroke="currentColor" stroke-width="2"/></svg>Upto 10k users</li>
        <li><svg width="16" height="12" viewBox="0 0 16 12"><path d="M1 6h13M9 1l5 5-5 5" fill="none" stroke="currentColor" stroke-width="2"/></svg>Upto 100 courses</li>
      </ul>
    </div>
    <div class="quote-button">REQUEST QUOTE</div>
  </article>

  <article class="plan enterprise">
    <div class="plan-name">ENTERPRISE</div>
    <div class="plan-scope">More than 100 courses</div>
    <div class="price"><span class="cur">$</span><span class="whole">1999</span><span class="cents">.00</span></div>
    <div class="features">
      <h3>Enterprise Features:</h3>
      <ul>
        <li><svg width="16" height="12" viewBox="0 0 16 12"><path d="M1 6h13M9 1l5 5-5 5" fill="none" stroke="currentColor" stroke-width="2"/></svg>For larger organizations</li>
        <li><svg width="16" height="12" viewBox="0 0 16 12"><path d="M1 6h13M9 1l5 5-5 5" fill="none" stroke="currentColor" stroke-width="2"/></svg>Scale learning globally</li>
        <li><svg width="16" height="12" viewBox="0 0 16 12"><path d="M1 6h13M9 1l5 5-5 5" fill="none" stroke="currentColor" stroke-width="2"/></svg>More than 10k users</li>
        <li><svg width="16" height="12" viewBox="0 0 16 12"><path d="M1 6h13M9 1l5 5-5 5" fill="none" stroke="currentColor" stroke-width="2"/></svg>More than 100 courses</li>
        <li><svg width="16" height="12" viewBox="0 0 16 12"><path d="M1 6h13M9 1l5 5-5 5" fill="none" stroke="currentColor" stroke-width="2"/></svg>Multiple instances</li>
      </ul>
    </div>
    <div class="quote-button">REQUEST QUOTE</div>
  </article>
</body>
</html>
```